Need a business card design for a new business

The business is going to be called "The Maple Lectern" - it is an online training company that provides Instructor Lead training to students at any destination in the world
The reference to cloud is the internet and classroom reference will be a computer at the students and instructors end

We will need a Web site and stationary and advertising material developed over time but for now require the business cards only

So if we are happy with the business card then we will use the same designers for the other requirments of the business as it evolves

Industry/Entity Type

Advertising

```html
<!DOCTYPE html>
<html lang="en">
<head>
<meta charset="utf-8">
<title>The Maple Lectern – Business Card</title>
<link rel="stylesheet" href="https://fonts.googleapis.com/css2?family=Arimo:wght@400;700&display=swap">
<style>
  :root {
    --backdrop: #5e1010;
    --card-white: #ffffff;
    --brand-blue: #0b56a8;
    --brand-blue-deep: #083c7d;
    --brand-blue-light: #1a6cc4;
    --ink-navy: #0a2f66;
    --panel-white: #fbfbfd;
  }
  * { box-sizing: border-box; margin: 0; padding: 0; }
  html, body {
    width: 1200px;
    height: 800px;
    overflow: hidden;
  }
  body {
    background: var(--backdrop);
    font-family: "Arimo", Arial, sans-serif;
    position: relative;
  }
  .card {
    position: absolute;
    width: 560px;
    height: 320px;
    overflow: hidden;
    box-shadow: 0 10px 24px rgba(0, 0, 0, 0.45);
  }

  /* Contact side */
  .card-contact {
    left: 60px;
    top: 120px;
    background: var(--card-white);
  }
  .brand {
    position: absolute;
    left: 250px;
    top: 78px;
    display: flex;
    align-items: center;
    gap: 10px;
  }
  .brand-dot {
    width: 26px;
    height: 26px;
    border-radius: 50%;
    background: var(--brand-blue);
  }
  .brand-name {
    font-weight: 700;
    font-size: 27px;
    color: var(--brand-blue);
    letter-spacing: -0.3px;
  }
  .contact-block {
    position: absolute;
    left: 0;
    bottom: 0;
    width: 290px;
    height: 170px;
    background: var(--brand-blue);
    border-radius: 0 150px 0 0 / 0 120px 0 0;
    padding: 42px 0 0 20px;
  }
  .contact-list {
    list-style: none;
    color: var(--card-white);
    font-weight: 700;
    font-size: 15px;
    line-height: 19px;
  }

  /* Name side */
  .card-name {
    left: 620px;
    top: 380px;
    background: linear-gradient(180deg, var(--brand-blue-light) 0%, var(--brand-blue) 45%, var(--brand-blue-deep) 100%);
  }
  .name-panel {
    position: absolute;
    left: 140px;
    top: 30px;
    width: 280px;
    height: 200px;
    background: var(--panel-white);
    border: 5px solid var(--brand-blue-deep);
    border-radius: 100px;
    display: flex;
    flex-direction: column;
    align-items: center;
    justify-content: center;
    text-align: center;
    color: var(--ink-navy);
  }
  .person-name {
    font-weight: 700;
    font-size: 44px;
    line-height: 46px;
  }
  .person-role {
    font-weight: 700;
    font-size: 20px;
    margin-top: 4px;
  }
  .web-strip {
    position: absolute;
    left: 0;
    bottom: 0;
    width: 100%;
    height: 46px;
    background: var(--card-white);
    display: flex;
    align-items: center;
    justify-content: center;
    font-weight: 700;
    font-size: 20px;
    color: var(--ink-navy);
  }
</style>
</head>
<body>
  <section class="card card-contact">
    <div class="brand">
      <span class="brand-dot"></span>
      <span class="brand-name">The Maple Lectern</span>
    </div>
    <div class="contact-block">
      <ul class="contact-list">
        <li>Tel: 000 000 000</li>
        <li>Mob: 1234 123 123</li>
        <li>Address line</li>
        <li>Address line</li>
        <li>yourname@maplemail.com</li>
      </ul>
    </div>
  </section>

  <section class="card card-name">
    <div class="name-panel">
      <p class="person-name">Your<br>Name</p>
      <p class="person-role">Position</p>
    </div>
    <div class="web-strip">www.maplelectern.com</div>
  </section>
</body>
</html>
```